corvane business cards

Hey design gurus!
I'm after a clean, modern, stylish business card for my about to be launched company.
I've uploaded the logos for my company "Corvane Electrical Solutions"
and also the brightway electricians logo to whom i am associated.

```html
<!DOCTYPE html>
<html lang="en">
<head>
<meta charset="utf-8">
<title>Corvane Electrical Solutions – Business Card</title>
<link rel="stylesheet" href="https://fonts.googleapis.com/css2?family=Montserrat:wght@400;500;600;700;800&display=swap">
<style>
  :root {
    --backdrop: #444444;
    --card-navy: #0a161f;
    --card-navy-deep: #08121a;
    --brand-blue: #1f8bd6;
    --text-white: #f2f4f6;
    --gold: #d9bc3c;
    --gold-line: #a8902c;
    --pattern-navy: #10222f;
  }
  * { box-sizing: border-box; margin: 0; padding: 0; }
  html, body {
    width: 1200px; height: 801px; overflow: hidden;
    background: var(--backdrop);
    font-family: "Montserrat", sans-serif;
  }
  .stage {
    position: relative; width: 1200px; height: 801px;
    display: flex; align-items: center; justify-content: center; gap: 40px;
  }
  .card {
    position: relative; width: 530px; height: 303px;
    background: var(--card-navy);
    border-bottom: 3px solid var(--brand-blue);
    overflow: hidden;
  }
  /* front */
  .brand {
    position: absolute; left: 34px; top: 36px;
    display: flex; align-items: center; gap: 14px;
    color: var(--brand-blue); font-weight: 800;
  }
  .brand-dot {
    width: 50px; height: 50px; border-radius: 50%;
    border: 4px solid var(--brand-blue);
  }
  .brand-name { font-size: 38px; letter-spacing: 2px; line-height: 1; }
  .brand-sub { font-size: 10.5px; letter-spacing: 3.4px; line-height: 1; margin-top: 5px; }
  .side-tab {
    position: absolute; left: 0; top: 130px;
    width: 30px; height: 24px; background: var(--brand-blue);
  }
  .contact {
    position: absolute; left: 46px; top: 128px;
    color: var(--text-white); font-size: 12.5px; line-height: 1.35;
  }
  .contact-name {
    color: var(--brand-blue); font-weight: 700; font-size: 18px;
    letter-spacing: 0.5px;
  }
  .contact-title { font-size: 13.5px; margin-bottom: 12px; }
  .contact-address { margin-bottom: 12px; }
  .contact-line { display: flex; align-items: center; gap: 8px; }
  .contact-line svg { width: 10px; height: 10px; fill: var(--brand-blue); }
  .partner {
    position: absolute; right: 34px; top: 108px;
    display: flex; align-items: center; gap: 12px;
    color: var(--gold); font-weight: 600;
  }
  .partner-square {
    width: 50px; height: 50px; border-radius: 6px; background: var(--gold);
  }
  .partner-name { font-size: 15px; line-height: 1.12; letter-spacing: 0.6px; }
  /* back */
  .card-back {
    background: linear-gradient(135deg, var(--pattern-navy), var(--card-navy-deep));
  }
</style>
</head>
<body>
<main class="stage">
  <section class="card card-front">
    <div class="brand">
      <span class="brand-dot"></span>
      <div>
        <div class="brand-name">CORVANE</div>
        <div class="brand-sub">ELECTRICAL SOLUTIONS</div>
      </div>
    </div>
    <span class="side-tab"></span>
    <div class="contact">
      <div class="contact-name">MARCUS HALE</div>
      <div class="contact-title">Managing Director</div>
      <div class="contact-address">Your address, City<br>State, Zip 1234</div>
      <div class="contact-line">
        <svg viewBox="0 0 10 10"><path d="M2 0h2l1 3-1.5 1a6 6 0 0 0 2.5 2.5L7 5l3 1v2a2 2 0 0 1-2 2A8 8 0 0 1 0 2a2 2 0 0 1 2-2z"/></svg>
        0400 555 218
      </div>
      <div class="contact-line">
        <svg viewBox="0 0 10 10"><path d="M0 2h10v6H0z"/></svg>
        info@corvanemail.com
      </div>
      <div class="contact-line">
        <svg viewBox="0 0 10 10"><circle cx="5" cy="5" r="5"/></svg>
        www.corvane-electrical.com
      </div>
    </div>
    <div class="partner">
      <span class="partner-square"></span>
      <div class="partner-name">BRONZE<br>BRIGHTWAY<br>ELECTRICIAN</div>
    </div>
  </section>
  <section class="card card-back" role="img" aria-label="Embossed repeating company mark pattern on dark navy"></section>
</main>
</body>
</html>
```